Pelling Home Efficiency

Id like for my business card to be very bold and professional. Incorporating the business logo, the main services offered, and my contact info. Services are spray foam, insulation, new construction, retrofit, weatherization.

When opening this project art huddle was not able to upload my new logo that I picked from another recent art huddle project. Does anyone know how i could upload my logo onto the page for design of the business cards?

Target Market(s)

Building owners, contractors

Industry/Entity Type

Building Insulation and performance improvements

Contact Information for Business Card

Owner, Email marcus@pellinghomeefficiency.com Phone number 555-204-6817

Colors
0054AA
0677BA
7BADD7
CADEEF
E8F1F8
F0912C
F2A743
F7CA91
FBE8D2
FDF5EE

Requirements
Must have
• Services- spray foam, cellulose, mineral wool, fiberglass, air sealing, new construction, retrofit, weatherization, energy saving assesments

```html
<!DOCTYPE html>
<html lang="en">
<head>
<meta charset="utf-8">
<title>Pelling Home Efficiency – Business Card</title>
<link rel="stylesheet" href="https://fonts.googleapis.com/css2?family=Montserrat:wght@500;800&family=Oswald:wght@500&family=Arimo:wght@400&display=swap">
<style>
  :root {
    --orange: #ee7623;
    --blue: #35b3e3;
    --ink: #111111;
    --paper: #ffffff;
    --backdrop: #d9d9d9;
  }
  * { margin: 0; padding: 0; box-sizing: border-box; }
  html, body { width: 1200px; height: 800px; overflow: hidden; }
  body {
    background: var(--backdrop);
    font-family: "Arimo", Arial, sans-serif;
    position: relative;
  }
  .card {
    position: absolute;
    background: var(--paper);
    border-radius: 26px;
    box-shadow: 0 4px 0 var(--orange), 0 14px 30px rgba(0,0,0,0.18);
  }
  /* Vertical info side */
  .card-info {
    left: 90px; top: 95px; width: 360px; height: 610px;
    padding: 36px 34px 30px;
    display: flex; flex-direction: column; align-items: center;
  }
  .brand {
    display: flex; align-items: center; gap: 12px;
    color: var(--orange);
    font-family: "Montserrat", Arial, sans-serif;
    font-weight: 800;
    text-transform: uppercase;
    line-height: 1.05;
  }
  .brand-mark { background: var(--blue); flex: none; }
  .card-info .brand { font-size: 22px; }
  .card-info .brand-mark { width: 22px; height: 22px; }
  .person { text-align: center; margin-top: 40px; }
  .person-name {
    font-family: "Montserrat", Arial, sans-serif;
    font-weight: 800; font-size: 32px; color: var(--orange);
  }
  .person-role { font-size: 22px; color: var(--ink); margin-top: 2px; }
  .icon-rule {
    display: flex; align-items: center; gap: 8px;
    width: 100%; margin: 14px 0 12px;
  }
  .icon-rule .rule { flex: 1; height: 2px; background: var(--orange); }
  .icon {
    width: 26px; height: 26px; border-radius: 50%;
    background: var(--blue);
    display: flex; align-items: center; justify-content: center;
  }
  .contact { text-align: center; font-size: 15px; line-height: 1.5; color: var(--ink); }
  .services-title {
    font-family: "Oswald", Arial, sans-serif;
    font-weight: 500; font-size: 28px; color: var(--orange);
    text-transform: uppercase; margin-top: 22px; letter-spacing: 0.5px;
  }
  .services {
    list-style: none; text-align: center;
    font-size: 16.5px; line-height: 1.42; color: var(--ink); margin-top: 8px;
  }
  /* Horizontal brand side */
  .card-brand {
    left: 500px; top: 225px; width: 620px; height: 355px;
    display: flex; align-items: center; justify-content: center;
  }
  .card-brand .brand { font-size: 40px; gap: 20px; }
  .card-brand .brand-mark { width: 40px; height: 40px; }
  .card-brand .brand-lines { display: flex; flex-direction: column; }
</style>
</head>
<body>

<section class="card card-info">
  <div class="brand">
    <span class="brand-mark"></span>
    <span>Pelling Home<br>Efficiency</span>
  </div>

  <div class="person">
    <div class="person-name">Marcus</div>
    <div class="person-role">Owner</div>
  </div>

  <div class="icon-rule">
    <span class="rule"></span>
    <span class="icon" aria-label="Phone">
      <svg width="14" height="14" viewBox="0 0 24 24"><path fill="#fff" d="M6.6 10.8a15.1 15.1 0 0 0 6.6 6.6l2.2-2.2a1 1 0 0 1 1-.25 11.4 11.4 0 0 0 3.6.57 1 1 0 0 1 1 1V20a1 1 0 0 1-1 1A17 17 0 0 1 3 4a1 1 0 0 1 1-1h3.5a1 1 0 0 1 1 1c0 1.25.2 2.45.57 3.57a1 1 0 0 1-.25 1z"/></svg>
    </span>
    <span class="icon" aria-label="Email">
      <svg width="14" height="14" viewBox="0 0 24 24"><rect x="3" y="6" width="18" height="12" rx="1.5" fill="#fff"/><path d="M3.5 7l8.5 6 8.5-6" stroke="#35b3e3" stroke-width="1.8" fill="none"/></svg>
    </span>
    <span class="icon" aria-label="Website">
      <svg width="14" height="14" viewBox="0 0 24 24"><circle cx="12" cy="12" r="9" fill="none" stroke="#fff" stroke-width="2"/><path d="M3 12h18M12 3c3 3 3 15 0 18M12 3c-3 3-3 15 0 18" stroke="#fff" stroke-width="1.6" fill="none"/></svg>
    </span>
    <span class="rule"></span>
  </div>

  <div class="contact">
    <div>555-204-6817</div>
    <div>marcus@pellinghomeefficiency.com</div>
    <div>www.pellinghomeefficiency.com</div>
  </div>

  <h2 class="services-title">Services Offered</h2>
  <ul class="services">
    <li>Spray foam</li>
    <li>Cellulose</li>
    <li>Mineral wool</li>
    <li>Fiberglass</li>
    <li>Air sealing</li>
    <li>New construction</li>
    <li>Retrofit</li>
    <li>Weatherization</li>
    <li>Energy saving assessments</li>
  </ul>
</section>

<section class="card card-brand">
  <div class="brand">
    <span class="brand-mark"></span>
    <span class="brand-lines"><span>Pelling Home</span><span>Efficiency</span></span>
  </div>
</section>

</body>
</html>
```